Shine Bay Auto Care Business Card

2 side business card design for an auto detailing business

Target Market(s)

Auto detailing

Contact Information for Business Card

Things included

The business name “Shine Bay Auto Care”
Marc Tessier
(403)261-9047
Riverton, Sk

Services offered - complete interior& exterior detail
- paint correction & protection
- ceramic coating
- trim restore
- auto carpet & seat cleaning

Requirements
Must have
• Colours that are in my logo

Services offered

My name Marc Tessier
403-261-9047
Riverton, Sk

Not too sure in what order for these ?
Website. Shinebayautocare.com
Instagram Shinebayautocare
Email. Shinebayautoac@mailbox-example.com

```html
<!DOCTYPE html>
<html lang="en">
<head>
<meta charset="utf-8">
<title>Shine Bay Auto Care – Business Card</title>
<link href="https://fonts.googleapis.com/css2?family=Montserrat:wght@400;500;600;700&display=swap" rel="stylesheet">
<style>
  :root {
    --red: #9b1c1f;
    --black: #050505;
    --white: #ffffff;
    --ink: #111111;
    --stage: #2a2a2a;
  }
  * { margin: 0; padding: 0; box-sizing: border-box; }
  html, body { width: 1200px; height: 780px; overflow: hidden; }
  body {
    background: var(--stage);
    font-family: "Montserrat", sans-serif;
    display: flex; flex-direction: column; align-items: center; justify-content: center; gap: 40px;
  }
  .card {
    position: relative; width: 600px; height: 343px;
    background: var(--white); border-radius: 26px; overflow: hidden;
  }
  .card-shapes { position: absolute; inset: 0; }

  .brand {
    position: absolute; display: flex; align-items: center; gap: 12px;
    font-weight: 700; text-transform: uppercase; letter-spacing: 1px;
  }
  .brand-dot { width: 34px; height: 34px; border-radius: 50%; border: 3px solid currentColor; flex: none; }
  .brand-name { font-size: 19px; line-height: 1.15; }
  .front .brand { left: 58px; top: 146px; color: var(--red); }
  .back .brand { left: 40px; top: 200px; color: var(--white); }

  /* Front: services */
  .services { position: absolute; right: 28px; top: 30px; width: 260px; list-style: none; }
  .service {
    display: flex; align-items: center; justify-content: flex-end; gap: 10px;
    color: var(--white); font-size: 11px; font-weight: 500; text-transform: uppercase;
    text-align: right; line-height: 1.2; height: 54px;
    border-bottom: 1px dotted var(--red);
  }
  .service:first-child { border-top: 1px dotted var(--red); }
  .service-mark { width: 16px; height: 16px; border-radius: 50%; border: 2px solid var(--red); flex: none; }

  /* Back: contact */
  .person { position: absolute; right: 60px; top: 34px; text-align: right; }
  .person-name { font-size: 28px; font-weight: 600; text-transform: uppercase; color: var(--ink); letter-spacing: -0.5px; }
  .person-name .surname { color: var(--red); }
  .person-role { font-size: 11px; font-weight: 500; letter-spacing: 3px; color: var(--ink); margin-top: 2px; }

  .contacts { position: absolute; right: 0; top: 100px; list-style: none; width: 290px; }
  .contact { display: flex; align-items: center; justify-content: flex-end; height: 26px; margin-bottom: 4px; }
  .contact-text { font-size: 11px; font-weight: 500; color: var(--ink); margin-right: 12px; white-space: nowrap; }
  .contact-tab {
    width: 52px; height: 22px; background: var(--red);
    display: flex; align-items: center; padding-left: 8px;
  }
  .contact-tab svg { width: 13px; height: 13px; }
  .contact.web { margin-top: 10px; }
</style>
</head>
<body>

  <section class="card front" aria-label="Business card front: services">
    <svg class="card-shapes" viewBox="0 0 600 343" aria-hidden="true">
      <circle cx="850" cy="40" r="578" fill="none" stroke="var(--red)" stroke-width="16" stroke-dasharray="130 12" />
      <circle cx="850" cy="40" r="560" fill="var(--black)" />
    </svg>
    <div class="brand">
      <span class="brand-dot"></span>
      <span class="brand-name">Shine Bay<br>Auto Care</span>
    </div>
    <ul class="services">
      <li class="service"><span>Complete Interior<br>&amp; Exterior Detail</span><span class="service-mark"></span></li>
      <li class="service"><span>Paint Correction<br>&amp; Protection</span><span class="service-mark"></span></li>
      <li class="service"><span>Ceramic Coating</span><span class="service-mark"></span></li>
      <li class="service"><span>Trim Restore</span><span class="service-mark"></span></li>
      <li class="service"><span>Auto Carpet &amp;<br>Seat Cleaning</span><span class="service-mark"></span></li>
    </ul>
  </section>

  <section class="card back" aria-label="Business card back: contact">
    <svg class="card-shapes" viewBox="0 0 600 343" aria-hidden="true">
      <circle cx="-200" cy="320" r="508" fill="none" stroke="var(--red)" stroke-width="16" stroke-dasharray="130 12" />
      <circle cx="-200" cy="320" r="490" fill="var(--black)" />
    </svg>
    <div class="brand">
      <span class="brand-dot"></span>
      <span class="brand-name">Shine Bay<br>Auto Care</span>
    </div>
    <div class="person">
      <p class="person-name">Marc <span class="surname">Tessier</span></p>
      <p class="person-role">Designation</p>
    </div>
    <ul class="contacts">
      <li class="contact"><span class="contact-text">(403)261-9047</span>
        <span class="contact-tab"><svg viewBox="0 0 16 16"><path fill="#fff" d="M3 1l3 3-1.5 2a8 8 0 0 0 5 5l2-1.5 3 3-2 2C6 14 2 10 1 3z"/></svg></span></li>
      <li class="contact"><span class="contact-text">Shinebayautoac@mailbox-example.com</span>
        <span class="contact-tab"><svg viewBox="0 0 16 16"><rect x="1" y="3" width="14" height="10" fill="none" stroke="#fff" stroke-width="1.5"/><path d="M1 3l7 6 7-6" fill="none" stroke="#fff" stroke-width="1.5"/></svg></span></li>
      <li class="contact"><span class="contact-text">Shinebayautocare</span>
        <span class="contact-tab"><svg viewBox="0 0 16 16"><rect x="2" y="2" width="12" height="12" fill="none" stroke="#fff" stroke-width="1.6"/></svg></span></li>
      <li class="contact"><span class="contact-text">Riverton, Sk</span>
        <span class="contact-tab"><svg viewBox="0 0 16 16"><path fill="#fff" d="M8 1a5 5 0 0 0-5 5c0 4 5 9 5 9s5-5 5-9a5 5 0 0 0-5-5zm0 7a2 2 0 1 1 0-4 2 2 0 0 1 0 4z"/></svg></span></li>
      <li class="contact web"><span class="contact-text">www.shinebayautocare.com</span>
        <span class="contact-tab"><svg viewBox="0 0 16 16" fill="none" stroke="#fff" stroke-width="1.3"><circle cx="8" cy="8" r="6.5"/><ellipse cx="8" cy="8" rx="3" ry="6.5"/><path d="M1.5 8h13M3 4.5h10M3 11.5h10"/></svg></span></li>
    </ul>
  </section>

</body>
</html>
```